Kestrel Photography Business Card

I need a business card designed for a photography business based in Perth, Western Australia called Kestrel Photography.

We specialise in wedding, event photography and portrait photography.

The business card must borrow the style of the attached logo.

The hex codes for the colours in the logo are:
#ED1D85 - Pink
#89C23E - Green
#37282F - Black

The name on the card will be:
Name: Toviran
Phone: 0417395268
Website: www.kestrelphotography.com.au
Facebook: kestrelphotography

I am open and happy to accept creative concepts.

I’d like some space at the back for writing notes and appointment details.

```html
<!DOCTYPE html>
<html lang="en">
<head>
<meta charset="utf-8">
<title>Kestrel Photography Business Card</title>
<link href="https://fonts.googleapis.com/css2?family=Questrial&family=Open+Sans:wght@400;700&display=swap" rel="stylesheet">
<style>
  :root {
    --pink: #ED1D85;
    --green: #89C23E;
    --lime: #9BE61E;
    --black: #0b0a0a;
    --ink: #37282F;
    --white: #ffffff;
    --pale-leaf: #eef6dc;
    --rule: #cfd8c0;
    --backdrop: #e9e7e4;
  }
  * { margin: 0; padding: 0; box-sizing: border-box; }
  html, body { width: 1200px; height: 1000px; overflow: hidden; }
  body {
    background: var(--backdrop);
    font-family: "Open Sans", Arial, sans-serif;
    position: relative;
  }
  .card {
    position: absolute;
    left: 240px;
    width: 720px;
    height: 420px;
    border-radius: 34px;
    overflow: hidden;
  }
  .card--front { top: 50px; background: var(--black); }
  .card--back { top: 530px; background: var(--white); }

  .ornament { position: absolute; }
  .ornament--leaf-crown {
    left: 290px; top: 0; width: 150px; height: 70px;
    background: radial-gradient(ellipse at 50% 20%, var(--lime) 0%, rgba(155,230,30,0.55) 55%, rgba(155,230,30,0) 75%);
  }
  .ornament--side-left {
    left: -40px; top: 60px; width: 230px; height: 340px;
    background: radial-gradient(ellipse at 40% 50%, #1c1b1b 0%, #121111 60%, rgba(11,10,10,0) 80%);
  }
  .ornament--side-right {
    right: -30px; top: 10px; width: 230px; height: 300px;
    background: radial-gradient(ellipse at 60% 45%, #1c1b1b 0%, #121111 60%, rgba(11,10,10,0) 80%);
  }
  .ornament--leaf-wreath {
    left: 60px; top: 20px; width: 600px; height: 380px;
    background: radial-gradient(ellipse at 55% 50%, var(--pale-leaf) 0%, rgba(238,246,220,0.7) 45%, rgba(238,246,220,0) 75%);
  }

  .brand-mark {
    position: absolute; left: 330px; top: 150px;
    width: 60px; height: 60px; border-radius: 50%;
    background: var(--pink);
  }
  .brand-name {
    position: absolute; left: 0; right: 0;
    font-family: "Questrial", "Century Gothic", sans-serif;
    text-transform: uppercase;
    letter-spacing: 0.55em;
    white-space: nowrap;
  }
  .card--front .brand-name { top: 240px; text-align: center; color: var(--white); font-size: 20px; padding-left: 0.55em; }
  .website {
    position: absolute; left: 0; right: 0; top: 330px;
    text-align: center; color: var(--lime);
    font-size: 19px; letter-spacing: 0.06em;
  }

  .card--back .brand-name { top: 44px; left: 60px; color: var(--black); font-size: 22px; }
  .notes {
    position: absolute; left: 60px; right: 40px; top: 100px;
    display: flex; flex-direction: column; gap: 34px;
  }
  .notes__line { height: 1px; background: var(--rule); }
  .person { position: absolute; left: 60px; top: 240px; }
  .person__name { color: var(--lime); font-weight: 700; font-size: 26px; letter-spacing: 0.08em; line-height: 1.1; }
  .person__role { color: var(--black); font-size: 19px; letter-spacing: 0.08em; }
  .contact {
    position: absolute; right: 40px; top: 262px;
    text-align: right; color: var(--black);
    font-size: 19px; letter-spacing: 0.1em; line-height: 1.4;
  }
  .contact__row { display: flex; align-items: center; justify-content: flex-end; gap: 8px; }
  .contact__icon { width: 16px; height: 18px; flex: none; }
  .services {
    position: absolute; left: 60px; right: 40px; top: 352px;
    display: flex; align-items: center; gap: 26px;
    color: var(--pink); font-size: 20px; letter-spacing: 0.12em;
    white-space: nowrap;
  }
  .services__divider { width: 1px; height: 22px; background: var(--ink); }
</style>
</head>
<body>
  <section class="card card--front">
    <div class="ornament ornament--leaf-crown" role="img" aria-label="Arc of green leaves"></div>
    <div class="ornament ornament--side-left" role="img" aria-label="Embossed black leaf ornament"></div>
    <div class="ornament ornament--side-right" role="img" aria-label="Embossed black leaf ornament"></div>
    <div class="brand-mark"></div>
    <p class="brand-name">Kestrel Photography</p>
    <p class="website">www.kestrelphotography.com.au</p>
  </section>

  <section class="card card--back">
    <div class="ornament ornament--leaf-wreath" role="img" aria-label="Faint pale green leaf pattern"></div>
    <p class="brand-name">Kestrel Photography</p>
    <div class="notes" aria-label="Space for notes and appointment details">
      <span class="notes__line"></span>
      <span class="notes__line"></span>
      <span class="notes__line"></span>
    </div>
    <div class="person">
      <p class="person__name">Toviran</p>
      <p class="person__role">Photographer</p>
    </div>
    <div class="contact">
      <p class="contact__row">0417395268
        <svg class="contact__icon" viewBox="0 0 16 18" aria-hidden="true"><rect x="3" y="1" width="10" height="16" rx="2" fill="none" stroke="#89C23E" stroke-width="2"/></svg>
      </p>
      <p class="contact__row">kestrelphotography
        <svg class="contact__icon" viewBox="0 0 16 18" aria-hidden="true"><rect x="0" y="1" width="16" height="16" rx="2" fill="#89C23E"/></svg>
      </p>
    </div>
    <div class="services">
      <span>wedding</span>
      <span class="services__divider"></span>
      <span>event</span>
      <span class="services__divider"></span>
      <span>and portrait photography</span>
    </div>
  </section>
</body>
</html>
```